Click Buttons for our website

We need a Click button design for our website www.brenvalo.dk:
- it should fit into our website's style and colors
- the buttons should be available in variable sizes (so they can accommodate from 1-7 word text)
- the buttons should be supplied as vector graphics (so we can resize them yourself)

The buttons are to replace the red text links we have on the site today, i.e. they are to be used to link to "contact us" page pdf's and such.

BrenVal is a Danish based IT Hosting and IT outsourcing Company selling business2business. our clients are medium sized companies with the need for It outsourcing.

```html
<!DOCTYPE html>
<html lang="en">
<head>
<meta charset="utf-8">
<title>Click Buttons</title>
<link rel="stylesheet" href="https://fonts.googleapis.com/css2?family=Ubuntu+Condensed&display=block">
<style>
  :root {
    --bg-dark-top: #1d1d1d;
    --bg-dark-bottom: #262626;
    --bg-light: #ffffff;
    --btn-top: #c6282b;
    --btn-mid: #b41a1d;
    --btn-low: #a60004;
    --btn-bottom: #970003;
    --btn-border: #6e0002;
    --btn-highlight: rgba(255, 255, 255, 0.28);
    --btn-text: #ffffff;
    --btn-text-shadow: rgba(60, 0, 0, 0.7);
    --btn-shadow-dark: rgba(0, 0, 0, 0.75);
    --btn-shadow-light: rgba(0, 0, 0, 0.45);
  }

  * { box-sizing: border-box; margin: 0; padding: 0; }

  html, body {
    width: 1200px;
    height: 900px;
    overflow: hidden;
  }

  .canvas {
    position: relative;
    width: 1200px;
    height: 900px;
    background: var(--bg-light);
    font-family: "Ubuntu Condensed", "Arial Narrow", "Roboto Condensed", sans-serif;
    font-stretch: condensed;
  }

  .theme {
    position: absolute;
    left: 0;
    width: 1200px;
  }

  .theme--dark {
    top: 0;
    height: 456px;
    background: linear-gradient(to bottom, var(--bg-dark-top), var(--bg-dark-bottom));
  }

  .theme--light {
    top: 456px;
    height: 444px;
    background: var(--bg-light);
  }

  .click-button {
    position: absolute;
    display: flex;
    align-items: center;
    justify-content: center;
    height: 70px;
    padding-top: 2px;
    border: 2px solid var(--btn-border);
    border-radius: 2px;
    background: linear-gradient(to bottom,
      var(--btn-top) 0%,
      var(--btn-mid) 48%,
      var(--btn-low) 52%,
      var(--btn-bottom) 100%);
    box-shadow: inset 0 2px 0 var(--btn-highlight);
    color: var(--btn-text);
    font-size: 32px;
    font-weight: 400;
    line-height: 1;
    text-decoration: none;
    text-transform: uppercase;
    text-shadow: 0 -1px 1px var(--btn-text-shadow);
    white-space: nowrap;
    overflow: hidden;
  }

  .theme--dark .click-button {
    box-shadow: inset 0 2px 0 var(--btn-highlight), 3px 4px 6px var(--btn-shadow-dark);
  }

  .theme--light .click-button {
    box-shadow: inset 0 2px 0 var(--btn-highlight), 3px 4px 5px var(--btn-shadow-light);
  }

  .click-button--short  { left: 480px; width: 200px; }
  .click-button--long   { left: 380px; width: 398px; }
  .click-button--medium { left: 442px; width: 278px; }

  .row-1 { top: 90px; }
  .row-2 { top: 220px; }
  .row-3 { top: 356px; }

  .theme--light .row-1 { top: 38px; }
  .theme--light .row-2 { top: 168px; }
  .theme--light .row-3 { top: 302px; }
</style>
</head>
<body>
  <main class="canvas">
    <section class="theme theme--dark" aria-label="Buttons on dark background">
      <a class="click-button click-button--short row-1" href="#">Kontakt</a>
      <a class="click-button click-button--long row-2" href="#">Lorem ipsum dolor</a>
      <a class="click-button click-button--medium row-3" href="#">Get in touch</a>
    </section>
    <section class="theme theme--light" aria-label="Buttons on light background">
      <a class="click-button click-button--short row-1" href="#">Kontakt</a>
      <a class="click-button click-button--long row-2" href="#">Lorem ipsum dolor</a>
      <a class="click-button click-button--medium row-3" href="#">Get in touch</a>
    </section>
  </main>
</body>
</html>
```